Business Card design for insurance broker in Denver, CO, USA

I need a business card designed using this logo that was just created. We sell life and disability income insurance to US consumers.
Looking for a professionally designed card to make use of the logo and have something to hand to prospects or new business referral sources. The card could be white, gray, black or whatever you would recommend.

Target Market(s)

US Consumers and other financial professionals that I partner with.

Industry/Entity Type

Insurance Broker

Contact Information for Business Card

Owen R. Tessler, CLU, LUTCF (please note that CLU should have a superscript R in a circle for registered trademark)
President
phone (303) 555-0147
email owen@brightlakecoverage.com
4620 W. Hollister Rd, Suite 310, Lakewood, CO 80226
Somewhere fit in a tagline saying "Trusted guidance for life, long term care, and income protection" (maybe the back if it doesn't fit on the front, your call)

Font styles to use
Sans Serif

Requirements
Must have
• Must have logo in correct blue and gray colors, my name, address, phone, email. Order and placement determined by the designer.
• I just want something that looks a more professional than what I could have done using the business card designer tool on printmakerhub.com or CardNest, or any other do-it-yourself tool
• A regular rectangular business card with square corners is preferred
Nice to have
• I included the logos of 2 organizations I belong to (GQLF and BEPWO). They should be small, but visible on the back only. If it doesn’t look good, this is not a requirement, feel free to drop it.
Should not have
• Do not add any colors not already in the logo, except use of black and whites which are okay. If you use the logo on the back and want to make that in all black, gray or white, that may be okay as well.

```html
<!DOCTYPE html>
<html lang="en">
<head>
<meta charset="utf-8">
<title>Brightlake Coverage – Business Card</title>
<link rel="stylesheet" href="https://fonts.googleapis.com/css2?family=Quicksand:wght@400;500;600;700&display=swap">
<style>
  :root {
    --stage: #616161;
    --brand-blue: #2a87c8;
    --white: #ffffff;
    --text-light: #f4f8fc;
    --muted: #a8a8a8;
  }
  * { box-sizing: border-box; margin: 0; padding: 0; }
  html, body { width: 1200px; height: 580px; overflow: hidden; }
  body {
    background: var(--stage);
    font-family: "Quicksand", sans-serif;
    position: relative;
  }
  .card {
    position: absolute;
    top: 166px;
    width: 416px;
    height: 260px;
    overflow: hidden;
  }
  .card--front { left: 166px; background: var(--white); }
  .card--back { left: 618px; background: var(--brand-blue); }

  /* brand lockup */
  .brand {
    position: absolute;
    display: flex;
    align-items: center;
  }
  .brand__mark {
    border-radius: 50%;
    border: 3px solid currentColor;
    flex: none;
  }
  .brand__name {
    font-weight: 700;
    text-transform: uppercase;
    line-height: 0.95;
    letter-spacing: 0.3px;
  }
  .card--front .brand { left: 12px; top: 17px; color: var(--brand-blue); }
  .card--front .brand__mark { width: 60px; height: 60px; margin-right: 14px; }
  .card--front .brand__name { font-size: 20px; }
  .card--back .brand { left: 74px; top: 70px; color: var(--white); }
  .card--back .brand__mark { width: 64px; height: 64px; margin-right: 36px; }
  .card--back .brand__name { font-size: 27px; }

  /* affiliation badges */
  .badges {
    position: absolute;
    top: 32px;
    left: 290px;
    display: flex;
    align-items: center;
    gap: 26px;
  }
  .badge {
    width: 40px;
    height: 32px;
    background: var(--brand-blue);
    border-radius: 3px;
  }
  .badge--round { border-radius: 50%; width: 34px; height: 34px; }

  /* identity */
  .person {
    position: absolute;
    left: 24px;
    top: 101px;
  }
  .person__name {
    color: var(--brand-blue);
    font-size: 16px;
    font-weight: 600;
  }
  .person__title {
    color: var(--muted);
    font-size: 11px;
    letter-spacing: 2.5px;
    margin-top: -1px;
  }

  /* contact band */
  .contact-band {
    position: absolute;
    left: 0; top: 136px;
    width: 100%;
    height: 97px;
    background: var(--brand-blue);
    list-style: none;
    padding: 15px 0 0 19px;
  }
  .contact-band li {
    display: flex;
    align-items: center;
    height: 24px;
    color: var(--text-light);
    font-size: 11.6px;
    font-weight: 400;
    white-space: nowrap;
  }
  .contact-band svg {
    width: 16px; height: 16px;
    margin-right: 10px;
    flex: none;
  }

  /* tagline strip */
  .tagline {
    position: absolute;
    left: 0; bottom: 0;
    width: 100%;
    height: 27px;
    background: var(--white);
    color: var(--brand-blue);
    font-size: 9.5px;
    font-weight: 500;
    letter-spacing: 1.9px;
    text-align: center;
    line-height: 27px;
    white-space: nowrap;
  }

  .back-email {
    position: absolute;
    left: 0; top: 186px;
    width: 100%;
    text-align: center;
    color: var(--text-light);
    font-size: 13px;
    letter-spacing: 1.2px;
  }
</style>
</head>
<body>

<section class="card card--front" aria-label="Business card front">
  <div class="brand">
    <span class="brand__mark"></span>
    <span class="brand__name">Brightlake<br>Coverage</span>
  </div>

  <div class="badges" aria-label="Professional affiliations">
    <span class="badge"></span>
    <span class="badge badge--round"></span>
  </div>

  <div class="person">
    <p class="person__name">Owen R. Tessler</p>
    <p class="person__title">President</p>
  </div>

  <ul class="contact-band">
    <li>
      <svg viewBox="0 0 16 16" aria-hidden="true"><path d="M8 1a5 5 0 0 0-5 5c0 3.6 5 9 5 9s5-5.4 5-9a5 5 0 0 0-5-5zm0 7a2 2 0 1 1 0-4 2 2 0 0 1 0 4z" fill="#fff"/></svg>
      4620 W. Hollister Rd, Suite 310, Lakewood, CO 80226
    </li>
    <li>
      <svg viewBox="0 0 16 16" aria-hidden="true"><path d="M3.5 1.5l2.5 3-1.5 1.8c.8 1.8 2.4 3.4 4.2 4.2L10.5 9l3 2.5-1.6 2.8C7 14 2 9 1.7 3.1z" fill="#fff"/><path d="M9.5 2.5a4 4 0 0 1 4 4M9.5 5a1.5 1.5 0 0 1 1.5 1.5" stroke="#fff" stroke-width="1.2" fill="none"/></svg>
      (303) 555-0147
    </li>
    <li>
      <svg viewBox="0 0 16 16" aria-hidden="true"><rect x="1" y="3" width="14" height="10" fill="none" stroke="#fff" stroke-width="1.3"/><path d="M1 3l7 6 7-6M1 13l5-5M15 13l-5-5" fill="none" stroke="#fff" stroke-width="1.3"/></svg>
      owen@brightlakecoverage.com
    </li>
  </ul>

  <p class="tagline">Trusted guidance for life, long term care, and income protection</p>
</section>

<section class="card card--back" aria-label="Business card back">
  <div class="brand">
    <span class="brand__mark"></span>
    <span class="brand__name">Brightlake<br>Coverage</span>
  </div>

  <p class="back-email">owen@brightlakecoverage.com</p>

  <p class="tagline">Trusted guidance for life, long term care, and income protection</p>
</section>

</body>
</html>
```